Glidewell Depot logo

Glidewell Depot is owned and operated by industry professionals with years of direct experience in providing customers with the right equipment to suit their needs. Our specialty lies within dealing in the Halvern Medical range of products. Our product range is suited to both the new user and for those that know what they want, a full line of products ranging from ultra-light wheelchairs, wheelchairs for sport and recreation and paediatric or just everyday use.

Industry/Entity Type

Recreation

Contact Information for Business Card

name, title, landline,fax,mobile,email,web address,physical address,logo,possibly a wheelchair pic

Requirements
Must have
• logo - uploaded
Nice to have
• colour scheme consistent with
www.glidewelldepot.com.au

```html
<!DOCTYPE html>
<html lang="en">
<head>
<meta charset="utf-8">
<title>Glidewell Depot – Business Card</title>
<link rel="stylesheet" href="https://fonts.googleapis.com/css2?family=Open+Sans:wght@400;600;700&display=swap">
<style>
  :root {
    --page-bg: #e9e6e1;
    --blue-light: #3f6fc4;
    --blue-mid: #2a52a8;
    --blue-dark: #1c3a8a;
    --card-white: #ffffff;
    --divider-grey: #c9ccd3;
    --brand-purple: #6a2d6e;
    --brand-teal: #2f8fb5;
    --text-light: #ffffff;
    --text-soft: #dce6fa;
  }
  * { box-sizing: border-box; margin: 0; padding: 0; }
  html, body {
    width: 1200px; height: 675px; overflow: hidden;
    background: var(--page-bg);
    font-family: "Open Sans", Arial, sans-serif;
  }
  .stage {
    width: 1200px; height: 675px;
    display: flex; align-items: center; justify-content: center;
  }
  .business-card {
    position: relative;
    width: 700px; height: 400px;
    border-radius: 6px;
    overflow: hidden;
    box-shadow: 0 14px 34px rgba(0,0,0,.22);
  }
  .card-background { position: absolute; inset: 0; }
  .brand-panel {
    position: absolute; left: 30px; top: 0; width: 330px; height: 400px;
    display: flex; flex-direction: column; align-items: center; justify-content: center;
    gap: 22px;
  }
  .brand-lockup { display: flex; align-items: center; gap: 14px; }
  .brand-dot {
    width: 44px; height: 44px; border-radius: 50%;
    background: var(--brand-teal);
  }
  .brand-name {
    color: var(--brand-purple);
    font-weight: 700; font-size: 34px; line-height: 1.05;
  }
  .brand-tagline {
    color: var(--brand-teal);
    font-size: 13px; font-weight: 600; letter-spacing: 1.2px;
  }
  .contact-panel {
    position: absolute; left: 420px; top: 58px; width: 260px;
    color: var(--text-light);
  }
  .person-name { font-size: 26px; font-weight: 700; }
  .person-title { font-size: 14px; color: var(--text-soft); margin-bottom: 26px; }
  .address { font-size: 14px; margin-bottom: 10px; }
  .contact-list { list-style: none; display: flex; flex-direction: column; gap: 8px; }
  .contact-item { display: flex; align-items: center; gap: 12px; font-size: 14px; }
  .contact-icon { width: 16px; height: 16px; flex: none; }
</style>
</head>
<body>
<main class="stage">
  <section class="business-card">
    <svg class="card-background" width="700" height="400" viewBox="0 0 700 400" aria-hidden="true">
      <defs>
        <linearGradient id="blueField" x1="0" y1="0" x2="1" y2="1">
          <stop offset="0" stop-color="var(--blue-light)"/>
          <stop offset="0.5" stop-color="var(--blue-mid)"/>
          <stop offset="1" stop-color="var(--blue-dark)"/>
        </linearGradient>
      </defs>
      <rect width="700" height="400" fill="url(#blueField)"/>
      <path d="M0 0 H340 Q430 200 340 400 H0 Z" fill="var(--divider-grey)"/>
      <path d="M0 0 H326 Q414 200 326 400 H0 Z" fill="var(--card-white)"/>
    </svg>

    <div class="brand-panel">
      <div class="brand-lockup">
        <span class="brand-dot"></span>
        <span class="brand-name">Glidewell<br>Depot</span>
      </div>
      <p class="brand-tagline">SERVICE - KNOWLEDGE - INNOVATION</p>
    </div>

    <div class="contact-panel">
      <h1 class="person-name">Aaron Pike</h1>
      <p class="person-title">Founder</p>
      <p class="address">Unit 8 14 Kestrel Lane, MARLOWE</p>
      <ul class="contact-list">
        <li class="contact-item">
          <svg class="contact-icon" viewBox="0 0 16 16"><rect x="4" y="1" width="8" height="14" rx="1.5" fill="none" stroke="#fff" stroke-width="1.5"/><circle cx="8" cy="12.5" r="0.9" fill="#fff"/></svg>
          +61 400 555 018
        </li>
        <li class="contact-item">
          <svg class="contact-icon" viewBox="0 0 16 16"><path d="M3 2 L6 2 L7 5 L5 6.5 Q6.5 9.5 9.5 11 L11 9 L14 10 L14 13 Q8 14 4 9 Q2 5.5 3 2 Z" fill="#fff"/></svg>
          +61 2 5550 1842
        </li>
        <li class="contact-item">
          <svg class="contact-icon" viewBox="0 0 16 16"><rect x="4" y="1.5" width="8" height="4" fill="#fff"/><rect x="1.5" y="6" width="13" height="6" rx="1" fill="#fff"/><rect x="4" y="10" width="8" height="4.5" fill="#fff" stroke="var(--blue-mid)" stroke-width="1"/></svg>
          +61 2 5550 1877
        </li>
        <li class="contact-item">
          <svg class="contact-icon" viewBox="0 0 16 16"><rect x="1.5" y="3.5" width="13" height="9" rx="1" fill="#fff"/><path d="M1.5 4 L8 9 L14.5 4" fill="none" stroke="var(--blue-mid)" stroke-width="1.2"/></svg>
          info@glidewelldepot.com.au
        </li>
        <li class="contact-item">
          <svg class="contact-icon" viewBox="0 0 16 16"><circle cx="8" cy="8" r="6.5" fill="none" stroke="#fff" stroke-width="1.4"/><ellipse cx="8" cy="8" rx="2.8" ry="6.5" fill="none" stroke="#fff" stroke-width="1.1"/><path d="M1.5 8 H14.5" stroke="#fff" stroke-width="1.1"/></svg>
          www.glidewelldepot.com.au
        </li>
      </ul>
    </div>
  </section>
</main>
</body>
</html>
```